Photography Business, Business Card

Looking for a unique cutting edge card that takes advantage of the latest printing technologies. Please review this site for all the options they office: https://plumeprints.example. If you can think it they can do it. And if you have an idea and do not know if they can do it, I will check into it.
Updates

Target Market(s)

People and places I took images of and future clients.

Industry/Entity Type

Photography

Contact Information for Business Card

Name, cell & email. Colin Hartley, chartley@kvnphoto.example, 318-742-9061

Colors

Designer to choose only greyscale colors for use in the design.

Requirements
Must have
• 100% cutting edge. Is so great, those I hand it to always show it to someone else. A piece of art.
Nice to have
• Blacks, silvers, greys, some red. Maybe other colors?

```html
<!DOCTYPE html>
<html lang="en">
<head>
<meta charset="utf-8">
<title>Colin Hartley Photography – Business Card</title>
<link href="https://fonts.googleapis.com/css2?family=Montserrat:wght@400;500;600&display=swap" rel="stylesheet">
<style>
  :root {
    --backdrop: #b7b7b7;
    --card: #323232;
    --card-shadow: rgba(0,0,0,0.45);
    --ink-dark: #0d0d0d;
    --ink-muted: #8a8a8a;
    --ink-light: #ffffff;
  }
  html, body {
    margin: 0;
    padding: 0;
    width: 1075px;
    height: 1200px;
    overflow: hidden;
    background: var(--backdrop);
    font-family: "Montserrat", Arial, sans-serif;
  }
  .canvas { position: relative; width: 1075px; height: 1200px; }
  .card {
    position: absolute;
    left: 207px;
    width: 665px;
    height: 397px;
    background: var(--card);
    box-shadow: 2px 3px 3px var(--card-shadow);
  }
  .card--front { top: 187px; border-top-right-radius: 118px; }
  .card--back { top: 640px; border-bottom-right-radius: 118px; }

  .cutout {
    position: absolute;
    width: 170px;
    height: 170px;
    border-radius: 50%;
    background: var(--backdrop);
    box-shadow: inset 2px 3px 4px rgba(0,0,0,0.35);
  }
  .card--front .cutout { left: 450px; top: 54px; }
  .card--back .cutout { left: 450px; top: 178px; }

  .wordmark {
    position: absolute;
    font-weight: 500;
    line-height: 1;
  }
  .wordmark__name { display: block; letter-spacing: 0.5px; }
  .wordmark__tag { display: block; letter-spacing: 3px; text-align: right; margin-top: 6px; }
  .card--front .wordmark { left: 34px; top: 78px; color: var(--ink-dark); }
  .card--front .wordmark__name { font-size: 40px; }
  .card--front .wordmark__tag { font-size: 11px; }
  .card--back .wordmark { left: 70px; top: 112px; color: var(--ink-light); }
  .card--back .wordmark__name { font-size: 46px; }
  .card--back .wordmark__tag { font-size: 12px; color: var(--ink-light); }

  .holder-name {
    position: absolute;
    left: 34px;
    top: 246px;
    margin: 0;
    font-size: 21px;
    font-weight: 600;
    color: var(--ink-muted);
  }
  .contact-list {
    position: absolute;
    left: 34px;
    top: 302px;
    margin: 0;
    padding: 0;
    list-style: none;
    color: var(--ink-muted);
    font-size: 16.5px;
    font-weight: 400;
  }
  .contact-list li { display: flex; align-items: center; height: 24px; }
  .contact-list svg { width: 16px; height: 16px; margin-right: 7px; fill: none; stroke: var(--ink-muted); stroke-width: 1.8; }

  .studio-mark {
    position: absolute;
    left: 436px;
    top: 318px;
    color: var(--ink-light);
    font-size: 38px;
    font-weight: 500;
    letter-spacing: 8px;
    line-height: 1;
  }
</style>
</head>
<body>
<div class="canvas">
  <section class="card card--front">
    <div class="wordmark">
      <span class="wordmark__name">Colin Hartley</span>
      <span class="wordmark__tag">PHOTOGRAPHY</span>
    </div>
    <div class="cutout"></div>
    <h2 class="holder-name">COLIN HARTLEY</h2>
    <ul class="contact-list">
      <li>
        <svg viewBox="0 0 16 16"><path d="M3 2 L6 2 L7 5 L5 6.5 C6 9 7 10 9.5 11 L11 9 L14 10 L14 13 C9 14 2 8 3 2 Z"/></svg>
        318-742-9061
      </li>
      <li>
        <svg viewBox="0 0 16 16"><rect x="1.5" y="3.5" width="13" height="9"/><path d="M1.5 3.5 L8 9 L14.5 3.5"/></svg>
        chartley@kvnphoto.example
      </li>
      <li>
        <svg viewBox="0 0 16 16"><circle cx="8" cy="8" r="6.5"/><ellipse cx="8" cy="8" rx="2.8" ry="6.5"/><path d="M1.5 8 H14.5"/></svg>
        www.kvnphoto.example
      </li>
    </ul>
    <div class="studio-mark">KVN</div>
  </section>

  <section class="card card--back">
    <div class="wordmark">
      <span class="wordmark__name">Colin Hartley</span>
      <span class="wordmark__tag">PHOTOGRAPHY</span>
    </div>
    <div class="cutout"></div>
  </section>
</div>
</body>
</html>
```